We are looking to recreate our Harmon & Company Jobsite Sign. This sign will be placed by the street at each of our jobsites. We want to keep this sign simple, but at the same time, want to add a catching appeal to the design for anyone passing by. We want to stick to a two color scheme (Harmon Blue, and White). Please only use the Company Logo that I have uploaded for this project. Please also see a mock up of what we would like to include on this sign. The Sign Dimensions will be 4' x 8'. Please keep all verbiage uniform with the verbiage on the sample design I have uploaded. LET YOUR CREATIVITY FLOW!

```html
<!DOCTYPE html>
<html lang="en">
<head>
<meta charset="utf-8">
<title>Harmon &amp; Company Jobsite Sign</title>
<link rel="stylesheet" href="https://fonts.googleapis.com/css2?family=Noticia+Text:wght@700&display=swap">
<style>
  :root {
    --harmon-blue: #1c1a98;
    --white: #ffffff;
    --backdrop: #d9d9d9;
    --backdrop-dark: #9a9a9a;
  }
  * { box-sizing: border-box; margin: 0; padding: 0; }
  html, body {
    width: 1000px; height: 1200px; overflow: hidden;
  }
  body {
    background: radial-gradient(circle at 70% 40%, var(--backdrop), var(--backdrop-dark));
    font-family: "Noticia Text", Georgia, serif;
    font-weight: 700;
    color: var(--harmon-blue);
    position: relative;
  }
  .jobsite-sign {
    position: absolute;
    left: 50px; top: 375px;
    width: 900px; height: 450px;
    background: var(--white);
    box-shadow: 0 12px 28px rgba(0,0,0,0.35);
    overflow: hidden;
  }
  .brand-name {
    position: absolute;
    left: 52px; top: 40px;
    width: 360px;
    text-align: center;
    line-height: 1;
  }
  .brand-name .primary { display: block; font-size: 84px; letter-spacing: -1px; }
  .brand-name .secondary { display: block; font-size: 34px; margin-top: 6px; }
  .brand-divider {
    position: absolute;
    left: 430px; top: 48px;
    width: 3px; height: 124px;
    background: var(--harmon-blue);
  }
  .trade-title {
    position: absolute;
    left: 450px; top: 50px;
    width: 380px;
    text-align: center;
    font-size: 52px;
    line-height: 1.08;
  }
  .slogan {
    position: absolute;
    left: 0; top: 188px;
    width: 100%;
    text-align: center;
    font-size: 46px;
    line-height: 1.1;
  }
  .slogan sup { font-size: 22px; vertical-align: 20px; }
  .info-band {
    position: absolute;
    left: 0; top: 293px;
    width: 100%; height: 157px;
    background: var(--harmon-blue);
  }
  .location-pill {
    position: absolute;
    left: 181px; top: 264px;
    width: 537px; height: 56px;
    background: var(--white);
    border: 2px solid var(--harmon-blue);
    border-radius: 28px;
    text-align: center;
    font-size: 32px;
    line-height: 52px;
    letter-spacing: 0.5px;
  }
  .phone {
    position: absolute;
    left: 0; top: 332px;
    width: 100%;
    text-align: center;
    color: var(--white);
    font-size: 31px;
    line-height: 1;
  }
  .phone svg { width: 26px; height: 26px; vertical-align: -3px; margin-right: 6px; }
  .social-links {
    position: absolute;
    left: 57px; top: 385px;
    display: flex; gap: 13px;
  }
  .social-links span {
    width: 36px; height: 36px;
    border-radius: 50%;
    background: var(--white);
  }
  .website {
    position: absolute;
    left: 290px; top: 386px;
    width: 330px;
    text-align: center;
    color: var(--white);
    font-size: 31px;
    line-height: 1;
  }
  .license {
    position: absolute;
    right: 57px; top: 392px;
    color: var(--white);
    font-size: 25px;
    line-height: 1;
  }
</style>
</head>
<body>
  <main class="jobsite-sign">
    <div class="brand-name">
      <span class="primary">Harmon</span>
      <span class="secondary">&amp; Company, Inc.</span>
    </div>
    <div class="brand-divider"></div>
    <h1 class="trade-title">General<br>Contractors</h1>
    <p class="slogan">“We Build Lasting Confidence”<sup>®</sup></p>
    <div class="info-band"></div>
    <div class="location-pill">MAPLEWOOD, FLORIDA</div>
    <p class="phone">
      <svg viewBox="0 0 26 26" aria-hidden="true">
        <circle cx="13" cy="13" r="11.5" fill="none" stroke="#fff" stroke-width="2"/>
        <path d="M9 7.5c1-.6 1.8 0 2.2 1l.6 1.6c.2.7-.2 1.2-.8 1.6.6 1.6 1.6 2.7 3.2 3.3.4-.6.9-1 1.6-.8l1.6.6c1 .4 1.5 1.2 1 2.2-.8 1.4-2.3 1.8-3.8 1.2-3.2-1.3-5.4-3.6-6.6-6.8C7.5 10 7.8 8.3 9 7.5z" fill="#fff"/>
      </svg>407-555-0148
    </p>
    <div class="social-links" aria-label="Social media links">
      <span></span><span></span><span></span>
    </div>
    <p class="website">HarmonCompany.net</p>
    <p class="license">CGC1594417</p>
  </main>
</body>
</html>
```